Business Card for Wellness Clinic

We need a business card for our new logo. I want it to match the feel of the logo

Target Market(s)

Young professional families looking for holistic health care

Industry/Entity Type

Health And Wellness

Contact Information for Business Card

Our business Name: Brackenfield Health & wellness Centre, our phone #, email address...see attached old business card

Font styles to use
Sans Serif

Colors
33b8a4
cee9f5

Requirements
Must have
• my logo and business name
• Font is "Helvetica Neue LT Std 45 Light" and
• Only for "&" using font "Trajan pro bold"
• Use colors in the logo

```html
<!DOCTYPE html>
<html lang="en">
<head>
<meta charset="utf-8">
<title>Brackenfield Health &amp; wellness Centre – Business Card</title>
<link rel="stylesheet" href="https://fonts.googleapis.com/css2?family=Source+Sans+3:wght@300;400;600&display=swap">
<style>
  :root {
    --backdrop: #3b3431;
    --card-dark: #111111;
    --teal: #33b8a4;
    --teal-deep: #2bb3a3;
    --text-light: #f2f2f2;
    --text-muted: #b9b9b9;
    --rule: #3a6f68;
  }
  * { margin: 0; padding: 0; box-sizing: border-box; }
  html, body {
    width: 1200px; height: 900px; overflow: hidden;
    background: var(--backdrop);
    font-family: "Source Sans 3", "Helvetica Neue", Arial, sans-serif;
    font-weight: 300;
  }
  .canvas { position: relative; width: 1200px; height: 900px; }

  .card {
    position: absolute; top: 300px;
    width: 525px; height: 300px;
    border-radius: 3px;
    box-shadow: 0 10px 28px rgba(0,0,0,.45);
  }
  .card--front { left: 50px; background: var(--card-dark); color: var(--text-light); }
  .card--back  { left: 625px; background: var(--teal-deep); display: flex; align-items: center; justify-content: center; }

  /* brand block */
  .brand {
    position: absolute; top: 38px; left: 0; width: 100%;
    display: flex; flex-direction: column; align-items: center; gap: 10px;
  }
  .brand__mark { width: 34px; height: 34px; background: var(--teal); border-radius: 4px; }
  .brand__name {
    color: var(--text-muted);
    font-size: 19px; letter-spacing: 4px; text-transform: uppercase;
    text-align: center; line-height: 1.35;
  }

  /* details */
  .details {
    position: absolute; top: 172px; left: 0; width: 100%;
    display: flex; justify-content: center;
  }
  .person {
    width: 230px; padding-right: 18px; text-align: right;
  }
  .person__name { color: var(--teal); font-weight: 600; font-size: 19px; line-height: 1.1; }
  .person__role { font-size: 15px; margin-bottom: 14px; }
  .person__address { font-size: 15px; line-height: 1.3; }
  .divider { width: 1px; height: 92px; background: var(--rule); }
  .contact { width: 240px; padding-left: 16px; list-style: none; font-size: 14px; }
  .contact__item { display: flex; align-items: center; gap: 8px; line-height: 1.45; }
  .contact__icon { width: 11px; height: 11px; fill: var(--teal); flex: none; }

  /* back */
  .back__name {
    color: #ffffff; font-size: 24px; letter-spacing: 4px;
    text-transform: uppercase; text-align: center; line-height: 1.4;
  }
</style>
</head>
<body>
<main class="canvas">

  <section class="card card--front" aria-label="Business card front">
    <header class="brand">
      <span class="brand__mark"></span>
      <p class="brand__name">Brackenfield Health<br>&amp; wellness Centre</p>
    </header>

    <div class="details">
      <div class="person">
        <p class="person__name">Daniel Harper</p>
        <p class="person__role">Managing Director</p>
        <p class="person__address">12345, Address Goes Here<br>Country Name, 123456.</p>
      </div>
      <span class="divider"></span>
      <ul class="contact">
        <li class="contact__item">
          <svg class="contact__icon" viewBox="0 0 24 24"><path d="M6.6 10.8a15 15 0 0 0 6.6 6.6l2.2-2.2a1 1 0 0 1 1-.25 11.4 11.4 0 0 0 3.6.57 1 1 0 0 1 1 1V20a1 1 0 0 1-1 1A17 17 0 0 1 3 4a1 1 0 0 1 1-1h3.5a1 1 0 0 1 1 1c0 1.25.2 2.45.57 3.57a1 1 0 0 1-.25 1z"/></svg>
          044-987 654 321
        </li>
        <li class="contact__item">
          <svg class="contact__icon" viewBox="0 0 24 24"><path d="M2 5h20v14H2z M2 5l10 8 10-8" stroke="#111" stroke-width="1.5"/></svg>
          info@brackenfieldhealth.com
        </li>
        <li class="contact__item">
          <svg class="contact__icon" viewBox="0 0 24 24"><circle cx="12" cy="12" r="10"/><path d="M2 12h20M12 2c3 3 3 17 0 20M12 2c-3 3-3 17 0 20" stroke="#111" stroke-width="1.5" fill="none"/></svg>
          www.brackenfieldhealth.com
        </li>
      </ul>
    </div>
  </section>

  <section class="card card--back" aria-label="Business card back">
    <p class="back__name">Brackenfield Health<br>&amp; wellness Centre</p>
  </section>

</main>
</body>
</html>
```